Professional Modern Website Design

We are a premium IT services provider to the financial industry based in London. Our company is called Veltra our current holding page is www.veltra-example.co.uk. We require a new website to match our new corporate identity. This project is for the design phase only. Development will be handled in-house. I have attached examples of wire frames we have developed (although open to suggestions for improvement) Our brand document that should demonstrate current brand, inc how we communicate to potential clients and finally mostly completed web-content.
We are looking for designers that can create something that sets us apart from our competitors.
Target Market(s)
IT Decision makers in Finance companies such as; hedge funds, private investment banks etc
Industry/Entity Type
Financial
Number of Pages Required
5+ page
Requirements
Must have
- hexagon elements in the design, unique design.
Nice to have
- Blog and social media feeds
Should not have
- Should not resemble a downloaded template

```html
<!DOCTYPE html>
<html lang="en">
<head>
<meta charset="utf-8">
<title>Veltra — IT Services for Finance</title>
<link href="https://fonts.googleapis.com/css2?family=Raleway:wght@300;400;500;600;700&display=swap" rel="stylesheet">
<style>
:root{
  --orange:#f7941d;
  --orange-deep:#f27a1a;
  --amber:#fbb034;
  --amber-card:#f9b31b;
  --slate:#555759;
  --ink:#2b2b2b;
  --muted:#7a7a7a;
  --night:#1c1f24;
  --white:#ffffff;
  --rule:#e4e4e4;
}
*{box-sizing:border-box;margin:0;padding:0}
html,body{width:1200px;height:3478px;overflow:hidden}
body{font-family:'Raleway',Arial,sans-serif;color:var(--ink);background:var(--white);position:relative}
section,header,footer,nav{position:relative;width:1200px}
.brand-name{font-family:'Raleway',Arial,sans-serif;font-weight:700;color:var(--orange);letter-spacing:1px}

/* hero */
.hero{height:772px;background:linear-gradient(160deg,#3a3f46 0%,#23272d 45%,#15181c 100%);color:var(--white);text-align:center;overflow:hidden}
.hero-backdrop{position:absolute;inset:0;background:linear-gradient(180deg,rgba(70,75,82,.55) 0%,rgba(20,22,26,.2) 40%,rgba(10,11,13,.6) 100%)}
.hero .brand-name{position:absolute;top:158px;left:0;width:100%;font-size:44px}
.hero h1{position:absolute;top:345px;left:0;width:100%;font-weight:400;font-size:32px}
.hero-lede{position:absolute;top:400px;left:300px;width:600px;font-size:16px;line-height:1.55;color:#e3e3e3}
.hero-arrow{position:absolute;top:338px}
.hero-arrow.prev{left:108px}.hero-arrow.next{right:108px}
.slider-dots{position:absolute;top:486px;left:0;width:100%;display:flex;justify-content:center;gap:10px}
.slider-dots span{width:8px;height:8px;border-radius:50%;background:#9a9ea4}
.slider-dots span.on{background:var(--white)}
.scroll-cue{position:absolute;top:524px;left:586px}

/* nav */
.site-nav{height:106px;border-bottom:1px solid var(--rule);background:var(--white)}
.site-nav .brand-name{position:absolute;left:110px;top:34px;font-size:30px}
.nav-links{position:absolute;right:110px;top:0;height:106px;display:flex;list-style:none}
.nav-links li{display:flex;align-items:center;padding:0 24px;font-size:13px;font-weight:600;letter-spacing:.5px}
.nav-links li.active{background:var(--orange);color:var(--white)}

/* who */
.who{height:220px;text-align:center}
.section-title{font-size:36px;font-weight:400;padding-top:72px}
.section-lede{width:620px;margin:18px auto 0;font-size:15px;line-height:1.6;color:var(--muted)}
.roles{display:flex;height:590px}
.role{width:300px;height:590px;color:var(--white);position:relative}
.role:nth-child(1){background:var(--orange)}
.role:nth-child(2){background:var(--amber)}
.role:nth-child(3){background:var(--orange-deep)}
.role:nth-child(4){background:var(--slate)}
.role h3{text-align:center;font-size:16px;font-weight:700;padding-top:48px;text-transform:uppercase}
.role p{text-align:center;font-size:12.5px;line-height:1.55;padding:14px 32px 0}
.role-portrait{position:absolute;left:0;bottom:0;width:300px;height:402px;background:linear-gradient(180deg,rgba(255,255,255,.0) 0%,rgba(40,40,45,.35) 100%)}
.role:nth-child(4) .role-portrait{background:linear-gradient(180deg,#5d6064 0%,#3b3d41 100%)}

/* about */
.about{height:466px;background:linear-gradient(165deg,#2a3038 0%,#1b1f25 55%,#121418 100%);color:var(--white)}
.about .section-title{padding-top:86px;text-align:center}
.about .section-lede{color:#c9c9c9;text-align:center;margin-top:12px}
.about-body{display:flex;gap:60px;margin:44px 0 0 120px;width:960px}
.about-lead{width:440px;font-size:22px;line-height:1.5;font-weight:400}
.about-detail{width:460px;font-size:13px;line-height:1.65;color:#c9c9c9}
.about-detail p+p{margin-top:14px}

/* services */
.services{height:556px;text-align:center}
.services .section-title{padding-top:90px}
.service-grid{display:flex;align-items:flex-start;gap:30px;margin:40px 0 0 120px;width:960px;text-align:left}
.service{width:300px;min-height:147px;display:flex;gap:16px;padding:22px 18px}
.service.featured{background:var(--amber-card);color:var(--white)}
.service h4{font-size:12.5px;font-weight:700;text-transform:uppercase;line-height:1.35}
.service p{font-size:12px;line-height:1.5;margin-top:8px;color:var(--muted)}
.service.featured p{color:var(--white)}
.service svg{flex:none}
.btn-more{display:block;width:96px;height:40px;line-height:40px;margin:44px auto 0;background:var(--orange);color:var(--white);font-size:13px;font-weight:700;text-align:center}

/* partners */
.partners{height:480px;background:linear-gradient(170deg,#2c2f34 0%,#1a1c20 60%,#101113 100%);color:var(--white);text-align:center}
.partners .section-title{padding-top:46px}
.partners .section-lede{color:#cfcfcf;margin-top:14px}
.partner-row{display:flex;justify-content:center;gap:62px;margin-top:50px}

/* footer */
.site-footer{height:288px;background:var(--white);display:flex;padding:50px 0 0 110px}
.footer-col{width:190px;font-size:12px;color:var(--muted)}
.footer-col h5{font-size:11px;font-weight:700;color:var(--ink);text-transform:uppercase;margin-bottom:12px}
.footer-col ul{list-style:none;line-height:1.9}
.footer-col p{line-height:1.8}
.footer-col .email{color:var(--orange)}
.social{display:flex;gap:8px}
.social span{width:18px;height:18px;background:var(--orange)}
.site-footer .brand-name{position:absolute;right:120px;top:95px;font-size:80px}
</style>
</head>
<body>

<header class="hero">
  <div class="hero-backdrop" role="img" aria-label="Looking up at glass office towers against a dark sky"></div>
  <span class="brand-name">Veltra</span>
  <svg class="hero-arrow prev" width="18" height="30" viewBox="0 0 18 30"><path d="M15 3 3 15l12 12" fill="none" stroke="#fff" stroke-width="3"/></svg>
  <svg class="hero-arrow next" width="18" height="30" viewBox="0 0 18 30"><path d="M3 3l12 12L3 27" fill="none" stroke="#fff" stroke-width="3"/></svg>
  <h1>You need integration. We’re always there with you.</h1>
  <p class="hero-lede">Veltra is one of the leading systems integrators to the world’s finance sector. We are an extension of your business and our services portfolio has been built so you always have access to a complete partner.</p>
  <div class="slider-dots"><span></span><span class="on"></span><span></span></div>
  <svg class="scroll-cue" width="28" height="44" viewBox="0 0 28 44"><rect x="2" y="2" width="24" height="40" rx="12" fill="none" stroke="#fff" stroke-width="2.5"/><line x1="14" y1="10" x2="14" y2="17" stroke="#fff" stroke-width="2.5"/></svg>
</header>

<nav class="site-nav">
  <span class="brand-name">Veltra</span>
  <ul class="nav-links">
    <li class="active">ABOUT</li><li>SERVICES</li><li>PARTNERS</li><li>CLIENTS</li><li>CONTACT</li>
  </ul>
</nav>

<section class="who">
  <h2 class="section-title">Who Are You</h2>
  <p class="section-lede">If you’re part of a financial organisation, we have the power to help everyone work more efficiently, productively and profitably.</p>
</section>

<section class="roles">
  <article class="role">
    <h3>Senior Hedge Fund Manager</h3>
    <p>You need to develop and implement strategies for business growth, while ensuring profitability. You’re aware your biggest asset is your staff and a happy workforce is a productive one.</p>
    <div class="role-portrait" role="img" aria-label="Portrait of a fund manager in a grey suit"></div>
  </article>
  <article class="role">
    <h3>CFO</h3>
    <p>Your key responsibility is to weigh the tradeoffs of IT costs against efficiency. We understand investment opportunities, providing they return higher efficiencies and revenue.</p>
    <div class="role-portrait" role="img" aria-label="Portrait of a finance director in a dark suit"></div>
  </article>
  <article class="role">
    <h3>IT Manager/CTO</h3>
    <p>Integration with partners and services is your key concern. You want to make sure any IT system you implement will work with the whole infrastructure of your company.</p>
    <div class="role-portrait" role="img" aria-label="Portrait of a technology manager with arms folded"></div>
  </article>
  <article class="role">
    <h3>Employees</h3>
    <p>Integration with partners and services is your key concern. You want to make sure any IT system you implement will work with the whole infrastructure of your company.</p>
    <div class="role-portrait" role="img" aria-label="Portrait of an employee in a suit and tie"></div>
  </article>
</section>

<section class="about" role="img" aria-label="Dark city skyline background">
  <h2 class="section-title">About Veltra</h2>
  <p class="section-lede">If we know something won’t benefit your business, we won’t do it.</p>
  <div class="about-body">
    <p class="about-lead">Veltra is one of the leading systems integrators to the world’s financial sector. We have more than 40 years’ experience working with high profile financial organisations. We always strive for mutual growth.</p>
    <div class="about-detail">
      <p>Consider us as an extension of your business. We work with you on a shared agenda to develop strategies and implement market leading solutions to strengthen your footprint against your competition.</p>
      <p>Our friendly and progressive approach to service brings you long-term, trusted relationships. We are always ready to help clients achieve their most important business objectives efficiently and maximise value for investment.</p>
    </div>
  </div>
</section>

<section class="services">
  <h2 class="section-title">Our Services</h2>
  <p class="section-lede">We are a world-class systems integrator with a wide range of expertise within the technology market, with no sector left unexplored.</p>
  <div class="service-grid">
    <div class="service featured">
      <svg width="56" height="62" viewBox="0 0 56 62"><polygon points="28,2 54,17 54,45 28,60 2,45 2,17" fill="none" stroke="#fff" stroke-width="2.5"/><rect x="18" y="22" width="20" height="16" fill="none" stroke="#fff" stroke-width="2"/></svg>
      <div><h4>Data Centre &amp; Infrastructure</h4><p>Ensure efficient supply, management and optimisation of your infrastructure to deliver your company’s productivity and profitability.</p></div>
    </div>
    <div class="service">
      <svg width="56" height="62" viewBox="0 0 56 62"><polygon points="28,2 54,17 54,45 28,60 2,45 2,17" fill="none" stroke="#f7941d" stroke-width="2.5"/><circle cx="28" cy="31" r="8" fill="none" stroke="#f7941d" stroke-width="2"/></svg>
      <div><h4>IT Support Manager and Professional Services</h4><p>Veltra built its reputation on IT support, managed and professional services and it continues to operate with these as a priority.</p></div>
    </div>
    <div class="service">
      <svg width="56" height="62" viewBox="0 0 56 62"><polygon points="28,2 54,17 54,45 28,60 2,45 2,17" fill="none" stroke="#f7941d" stroke-width="2.5"/><path d="M20 24c3 8 8 13 16 16l3-4-5-3-2 2c-3-2-5-4-7-7l2-2-3-5z" fill="#f7941d"/></svg>
      <div><h4>Voice &amp; Data Networks</h4><p>Veltra can offer hosted voice over IP (VoIP) and more traditional PBX systems based around a flexible, reliable and scalable platform.</p></div>
    </div>
  </div>
  <span class="btn-more">MORE</span>
</section>

<section class="partners" role="img" aria-label="Dark city street scene background">
  <h2 class="section-title">Partners</h2>
  <p class="section-lede">We have carefully selected our partners to help your business grow how you want it to. All our partners have the same values as we do, making sure their solutions seamlessly integrate with your organisation.</p>
  <div class="partner-row">
    <svg width="100" height="112" viewBox="0 0 100 112"><polygon points="50,3 97,30 97,82 50,109 3,82 3,30" fill="none" stroke="#fff" stroke-width="2"/></svg>
    <svg width="100" height="112" viewBox="0 0 100 112"><polygon points="50,3 97,30 97,82 50,109 3,82 3,30" fill="none" stroke="#fff" stroke-width="2"/></svg>
    <svg width="100" height="112" viewBox="0 0 100 112"><polygon points="50,3 97,30 97,82 50,109 3,82 3,30" fill="none" stroke="#fff" stroke-width="2"/></svg>
    <svg width="100" height="112" viewBox="0 0 100 112"><polygon points="50,3 97,30 97,82 50,109 3,82 3,30" fill="none" stroke="#fff" stroke-width="2"/></svg>
    <svg width="100" height="112" viewBox="0 0 100 112"><polygon points="50,3 97,30 97,82 50,109 3,82 3,30" fill="none" stroke="#fff" stroke-width="2"/></svg>
    <svg width="100" height="112" viewBox="0 0 100 112"><polygon points="50,3 97,30 97,82 50,109 3,82 3,30" fill="none" stroke="#fff" stroke-width="2"/></svg>
  </div>
</section>

<footer class="site-footer">
  <div class="footer-col">
    <h5>Navigation</h5>
    <ul><li>Home</li><li>About</li><li>Services</li><li>Partners</li><li>Clients</li><li>Contact</li></ul>
  </div>
  <div class="footer-col">
    <h5>Contact Us</h5>
    <p>48 Harlow Street<br>London, EC3M 4AB<br>United Kingdom</p>
    <p style="margin-top:10px">+44 20 7946 0185</p>
    <p class="email" style="margin-top:10px">hello@veltra-example.co.uk</p>
  </div>
  <div class="footer-col">
    <h5>Connect</h5>
    <div class="social"><span></span><span></span></div>
  </div>
  <span class="brand-name">Veltra</span>
</footer>

</body>
</html>
```